Brevin Finance Flyer Design

I would like a high res flyer designed for mass printing. It is for a mortgage and finance broking company in Sydney. We are called Brevin Finance. The wording i would like displayed is the following
Looking For Something Extra from your broker?
Brevin Finance can make all the difference
What we offer you is an extensive range of mortgage and finance products, including:
• Home Loans
• Investment Loans
• Low Doc Loans
• Vehicle Finance
• Equipment Finance
• Commercial Loans
• Refinance
Contact Us
Phone (02) 7354 2816
email info@brevinfinance.com.au
web www.brevinfinance.com.au
Finance

```html
<!DOCTYPE html>
<html lang="en">
<head>
<meta charset="utf-8">
<title>Brevin Finance Flyer</title>
<link rel="stylesheet" href="https://fonts.googleapis.com/css2?family=Noto+Sans:wght@400;700&family=Open+Sans:wght@400&display=swap">
<style>
  :root {
    --charcoal: #3a3d40;
    --navy: #0f2170;
    --navy-text: #1b2a78;
    --ink: #111111;
    --body: #222222;
    --brand-grey: #3d4044;
    --white: #ffffff;
  }
  * { margin: 0; padding: 0; box-sizing: border-box; }
  html, body { width: 846px; height: 1200px; overflow: hidden; background: var(--white); }
  .flyer {
    position: relative; width: 846px; height: 1200px; overflow: hidden;
    background: var(--white); font-family: "Noto Sans", sans-serif; color: var(--body);
  }
  .hero-photo {
    position: absolute; left: 0; top: 100px; width: 846px; height: 630px;
    background: linear-gradient(90deg, #e2ebf1 0%, #f4f8fb 30%, #e9eff5 50%, #aeb9d6 62%, #3c4c98 76%, #25357f 88%, #9aa7cc 100%);
  }
  .offer-panel {
    position: absolute; left: 30px; top: 706px; width: 680px; height: 30px; background: var(--white);
  }
  .top-band, .bottom-band { position: absolute; left: 0; width: 846px; }
  .top-band { top: 0; height: 140px; }
  .bottom-band { top: 1050px; height: 150px; }
  .tagline-question {
    position: absolute; top: 35px; left: 0; width: 846px; text-align: center;
    font-family: "Open Sans", sans-serif; font-size: 32.5px; color: var(--white);
  }
  .headline { position: absolute; left: 105px; top: 160px; color: var(--navy-text); font-weight: 400; }
  .headline-lead { font-size: 31px; line-height: 40px; }
  .headline-lead strong { font-weight: 700; }
  .headline-main { font-size: 40px; line-height: 46px; font-weight: 700; color: var(--ink); }
  .offer-intro { position: absolute; left: 54px; top: 714px; color: var(--navy-text); font-size: 22.3px; line-height: 30px; }
  .offer-intro strong { font-weight: 700; }
  .product-list { position: absolute; left: 117px; top: 798px; list-style: none; font-size: 21px; line-height: 33px; color: var(--body); }
  .brand { position: absolute; left: 388px; top: 942px; width: 430px; }
  .brand-name { display: flex; align-items: center; gap: 14px; font-size: 50px; line-height: 56px; color: var(--brand-grey); font-weight: 400; }
  .brand-square { width: 40px; height: 40px; background: var(--brand-grey); }
  .brand-tagline { margin-left: 68px; font-size: 16.5px; color: var(--brand-grey); }
  .contact { position: absolute; left: 117px; top: 1111px; color: var(--white); }
  .contact-phone { font-size: 25.5px; font-weight: 700; line-height: 34px; }
  .contact-online { font-size: 19.3px; line-height: 34px; margin-top: 2px; }
  .contact-online span + span { margin-left: 10px; }
</style>
</head>
<body>
<div class="flyer">
  <div class="hero-photo" role="img" aria-label="Photograph of business people walking through a bright office corridor"></div>
  <div class="offer-panel"></div>

  <svg class="top-band" viewBox="0 0 846 140" aria-hidden="true">
    <polygon points="0,0 846,0 846,104 390,104 305,134 220,104 0,104" fill="var(--charcoal)"/>
    <polyline points="218,104 305,134 392,104" fill="none" stroke="var(--navy)" stroke-width="4"/>
  </svg>
  <p class="tagline-question">Looking For Something Extra from your broker?</p>

  <h1 class="headline">
    <span class="headline-lead"><strong>Brevin Finance</strong> can make</span><br>
    <span class="headline-main">all the difference</span>
  </h1>

  <p class="offer-intro">What we offer you is<br><strong>an extensive range of mortgage and finance products</strong></p>

  <ul class="product-list">
    <li>Home Loans</li>
    <li>Investment Loans</li>
    <li>Low Doc Loans</li>
    <li>Vehicle Finance</li>
    <li>Equipment Finance</li>
    <li>Commercial Loans</li>
    <li>Refinance</li>
  </ul>

  <div class="brand">
    <div class="brand-name"><span class="brand-square"></span>BrevinFinance</div>
    <div class="brand-tagline">mortgage and finance broking services</div>
  </div>

  <svg class="bottom-band" viewBox="0 0 846 150" aria-hidden="true">
    <polygon points="0,44 530,44 627,10 725,44 846,44 846,150 0,150" fill="var(--navy)"/>
    <polyline points="0,42 530,42 627,8 725,42 846,42" fill="none" stroke="#000" stroke-width="4"/>
  </svg>

  <div class="contact">
    <p class="contact-phone">Phone (02) 7354 2816</p>
    <p class="contact-online"><span>email info@brevinfinance.com.au</span><span>web www.brevinfinance.com.au</span></p>
  </div>
</div>
</body>
</html>
```